Business card - Brio Margin - size 85 mm * 55 mm

We need new business cards. Design must fit with our vision of the firm. You find in the attached file our logo and a short description of our firm (mission, vision, value, business and so on).

Target Market(s)

Consulting firm in performance improvement

Industry/Entity Type

Management Consulting

Contact Information for Business Card

SIZE
85 mm * 55 mm
INFORMATIONS
name surname
role position
telephone number
email address

Requirements
Must have
• the brand must APPEAR for the rest Would we like to have something sleek, inspired to a "just right" approach
Should not have
• Please avoid the black color as background

```html
<!DOCTYPE html>
<html lang="en">
<head>
<meta charset="utf-8">
<title>Brio Margin – Business Cards</title>
<link rel="stylesheet" href="https://fonts.googleapis.com/css2?family=Montserrat:wght@400;500;600;700&display=swap">
<style>
  :root {
    --backdrop: #232323;
    --card: #3c3c3c;
    --orange: #f26a21;
    --sage: #6f8a74;
    --text-light: #e8e8e8;
    --text-muted: #cfcfcf;
  }
  * { margin: 0; padding: 0; box-sizing: border-box; }
  html, body {
    width: 1200px; height: 900px; overflow: hidden;
    background: var(--backdrop);
    font-family: "Montserrat", Arial, sans-serif;
  }
  .canvas { position: relative; width: 1200px; height: 900px; }
  .card {
    position: absolute;
    width: 560px; height: 362px;
    background: var(--card);
    border-radius: 22px;
  }
  .card--front { left: 80px; top: 70px; }
  .card--back { left: 560px; top: 468px; }

  /* Front */
  .front-brand {
    position: absolute; left: 0; right: 0; top: 118px;
    display: flex; align-items: center; justify-content: center; gap: 16px;
  }
  .brand-dot {
    width: 46px; height: 46px; border-radius: 50%;
    border: 5px solid var(--sage);
  }
  .brand-name {
    color: var(--orange); font-weight: 700; font-size: 34px; letter-spacing: 2px;
  }
  .front-url {
    position: absolute; left: 0; right: 0; top: 262px;
    text-align: center; color: var(--text-light);
    font-size: 17px; font-weight: 500; letter-spacing: 0.5px;
  }
  .front-url strong { color: var(--orange); font-weight: 700; }

  /* Back */
  .back-brand {
    position: absolute; left: 48px; top: 120px;
    display: flex; flex-direction: column; align-items: center; gap: 18px;
  }
  .back-brand .brand-dot { width: 58px; height: 58px; }
  .back-brand .brand-name {
    font-size: 19px; font-weight: 600; letter-spacing: 8px;
  }
  .contact { position: absolute; left: 318px; top: 104px; }
  .contact-name {
    color: var(--orange); font-weight: 600; font-size: 21px; letter-spacing: 0.5px;
  }
  .contact-role { color: var(--text-muted); font-size: 14px; margin: 4px 0 12px; }
  .contact-list { list-style: none; }
  .contact-item {
    display: flex; align-items: center; gap: 10px;
    color: var(--text-light); font-size: 14.5px; line-height: 24px;
  }
  .contact-item svg { width: 12px; height: 12px; flex: none; }
  .contact-item strong { color: var(--orange); font-weight: 600; }
</style>
</head>
<body>
<main class="canvas">
  <section class="card card--front">
    <div class="front-brand">
      <span class="brand-dot"></span>
      <span class="brand-name">BRIO MARGIN</span>
    </div>
    <p class="front-url">www.<strong>briomargin</strong>.com</p>
  </section>

  <section class="card card--back">
    <div class="back-brand">
      <span class="brand-dot"></span>
      <span class="brand-name">BRIO MARGIN</span>
    </div>
    <div class="contact">
      <h1 class="contact-name">MARCO ELLERY</h1>
      <p class="contact-role">Director</p>
      <ul class="contact-list">
        <li class="contact-item">
          <svg viewBox="0 0 12 12" aria-hidden="true"><path d="M2 1h2.5l1 3-1.5 1a6 6 0 0 0 3 3l1-1.5 3 1V10a1 1 0 0 1-1 1A9 9 0 0 1 1 2a1 1 0 0 1 1-1z" fill="var(--orange)"/></svg>
          +330 4172-8815
        </li>
        <li class="contact-item">
          <svg viewBox="0 0 12 12" aria-hidden="true"><rect x="1" y="2.5" width="10" height="7" rx="1" fill="none" stroke="var(--orange)" stroke-width="1.3"/><path d="M1.5 3l4.5 3.5L10.5 3" fill="none" stroke="var(--orange)" stroke-width="1.3"/></svg>
          info@briomargin.com
        </li>
        <li class="contact-item">
          <svg viewBox="0 0 12 12" aria-hidden="true"><circle cx="6" cy="6" r="5" fill="var(--orange)"/><path d="M1 6h10M6 1c-2.5 3-2.5 7 0 10M6 1c2.5 3 2.5 7 0 10" fill="none" stroke="var(--card)" stroke-width="0.8"/></svg>
          www.<strong>briomargin</strong>.com
        </li>
      </ul>
    </div>
  </section>
</main>
</body>
</html>
```